" ELA NAO FOI ABERTA AINDA MAS SERA EM 20 DIAS. A VARTEMI - uma empresa especializada na prestação de serviços terceirizados integrados, auxiliando nossos clientes a reduzir custos indiretos, focar em seu negócio principal, sem se preocupar com serviços de apoio, como limpeza, copa, portaria, segurança, administrativo, zeladoria, telefonia e recepção. Uma empresa ou Condomínio apresenta necessidades diversas para se manter operando de maneira lucrativa e segura. Antes, cada negócio precisava atender às demandas por meio de sua infraestrutura interna. Mas uma opção vantajosa vem crescendo no mercado e merece destaque atualmente: a terceirização de atividades "

```html
<!DOCTYPE html>
<html lang="pt-BR">
<head>
<meta charset="UTF-8">
<title>VARTEMI – Envelopes</title>
<link href="https://fonts.googleapis.com/css2?family=Raleway:wght@400;500;700&display=swap" rel="stylesheet">
<style>
  :root {
    --bg: #2b2b2d;
    --paper: #ffffff;
    --paper-shade: #ececec;
    --ink: #1a1a1a;
    --black: #0d0d0d;
    --black-soft: #1c1c1c;
    --gold: #b9a23a;
    --gold-light: #d8c565;
    --gold-dark: #7d6c1e;
    --text-grey: #555555;
  }
  * { box-sizing: border-box; margin: 0; padding: 0; }
  html, body { width: 1200px; height: 1200px; overflow: hidden; }
  body {
    background: var(--bg);
    font-family: "Raleway", sans-serif;
    position: relative;
  }
  .envelope {
    position: absolute;
    left: 204px;
    width: 792px;
    overflow: hidden;
  }
  .envelope--back {
    top: 252px;
    height: 360px;
    background: linear-gradient(180deg, var(--paper) 0%, var(--paper) 60%, var(--paper-shade) 100%);
  }
  .envelope--front {
    top: 622px;
    height: 345px;
    background: linear-gradient(135deg, var(--black-soft) 0%, var(--black) 70%);
  }
  .flap { position: absolute; left: 0; top: 0; width: 792px; height: 92px; }
  .brand-name {
    position: absolute;
    font-weight: 700;
    color: var(--gold);
    letter-spacing: 4px;
    display: flex;
    align-items: center;
    gap: 8px;
  }
  .brand-name .mark {
    width: 8px; height: 8px; border-radius: 50%; background: var(--gold);
  }
  .envelope--back .brand-name {
    top: 48px; left: 0; width: 100%; justify-content: center; font-size: 26px;
  }
  .envelope--front .brand-name {
    top: 96px; left: 48px; font-size: 28px;
  }
  .envelope--front .brand-name .mark { width: 12px; height: 12px; border-radius: 0; }
  .emblem-area {
    position: absolute;
    border-radius: 46% 40% 20% 30%;
  }
  .envelope--back .emblem-area {
    right: 36px; top: 110px; width: 300px; height: 250px;
    background: radial-gradient(ellipse at 50% 40%, rgba(200,200,200,0.55) 0%, rgba(225,225,225,0.25) 60%, rgba(255,255,255,0) 80%);
  }
  .envelope--front .emblem-area {
    right: 40px; top: 20px; width: 340px; height: 290px;
    background: radial-gradient(ellipse at 50% 40%, rgba(60,60,60,0.55) 0%, rgba(40,40,40,0.25) 60%, rgba(0,0,0,0) 80%);
  }
  .contact-row {
    position: absolute;
    left: 118px; top: 268px;
    display: flex; gap: 60px;
    font-size: 9.5px; color: var(--text-grey); line-height: 1.35;
  }
  .contact-item { display: flex; gap: 8px; align-items: flex-start; }
  .contact-item svg { width: 14px; height: 14px; flex: none; }
  .gold-band { position: absolute; left: 0; bottom: 0; width: 792px; height: 30px; }
</style>
</head>
<body>
  <section class="envelope envelope--back">
    <div class="emblem-area" role="img" aria-label="Faint large emblem decoration in light grey"></div>
    <svg class="flap" viewBox="0 0 792 92" aria-hidden="true">
      <path d="M0,0 H792 V56 Q792,84 764,84 H28 Q0,84 0,56 Z" fill="#0d0d0d"/>
    </svg>
    <div class="brand-name">VARTEMI<span class="mark"></span></div>
    <div class="contact-row">
      <div class="contact-item">
        <svg viewBox="0 0 14 14"><circle cx="7" cy="7" r="6.5" fill="none" stroke="#333"/><path d="M7,3.5a2.2,2.2 0 0 1 2.2,2.2c0,1.7-2.2,4.3-2.2,4.3s-2.2-2.6-2.2-4.3A2.2,2.2 0 0 1 7,3.5z" fill="#333"/></svg>
        <div>VARTEMI SERVIÇOS TERCEIRIZADOS LTDA<br>Rua das Acácias 1820<br>Jardim Aurora Niterói - RJ<br>CEP 24000-100</div>
      </div>
      <div class="contact-item">
        <svg viewBox="0 0 14 14"><circle cx="7" cy="7" r="6.5" fill="none" stroke="#333"/><rect x="3.5" y="4.5" width="7" height="5" fill="none" stroke="#333"/><path d="M3.5,4.5 L7,7.5 L10.5,4.5" fill="none" stroke="#333"/></svg>
        <div>contato@vartemi.com.br</div>
      </div>
      <div class="contact-item">
        <svg viewBox="0 0 14 14"><circle cx="7" cy="7" r="6.5" fill="none" stroke="#333"/><path d="M4.6,4 L6,4 L6.6,5.6 L5.8,6.3 Q6.6,7.8 7.8,8.3 L8.5,7.5 L10,8.1 L10,9.5 Q7.5,10.2 5.6,8.2 Q3.9,6.4 4.6,4 Z" fill="#333"/></svg>
        <div>(21) 90000-1234</div>
      </div>
    </div>
    <svg class="gold-band" viewBox="0 0 792 30" preserveAspectRatio="none" aria-hidden="true">
      <defs><linearGradient id="goldA" x1="0" x2="1"><stop offset="0" stop-color="#7d6c1e"/><stop offset="0.5" stop-color="#d8c565"/><stop offset="1" stop-color="#7d6c1e"/></linearGradient></defs>
      <path d="M0,22 H150 Q162,22 170,12 Q176,4 190,4 H600 Q614,4 620,12 Q628,22 640,22 H792 V30 H0 Z" fill="url(#goldA)"/>
    </svg>
  </section>

  <section class="envelope envelope--front">
    <div class="emblem-area" role="img" aria-label="Faint large emblem decoration in dark grey"></div>
    <div class="brand-name"><span class="mark"></span>VARTEMI</div>
    <svg class="gold-band" viewBox="0 0 792 30" preserveAspectRatio="none" aria-hidden="true">
      <defs><linearGradient id="goldB" x1="0" x2="1"><stop offset="0" stop-color="#7d6c1e"/><stop offset="0.5" stop-color="#d8c565"/><stop offset="1" stop-color="#7d6c1e"/></linearGradient></defs>
      <path d="M0,22 H150 Q162,22 170,12 Q176,4 190,4 H600 Q614,4 620,12 Q628,22 640,22 H792 V30 H0 Z" fill="url(#goldB)"/>
    </svg>
  </section>
</body>
</html>
```